Vengo Cantando(the singer)

We are a Christian Salsa Band in Chicago named Orquesta BRIZA (orchestra breeze). We are done with our single and we need a design for our CD cover. not anything specific just want something nice and I need it yesterday.

Industry/Entity Type

Christian

```html
<!DOCTYPE html>
<html lang="es">
<head>
<meta charset="utf-8">
<title>Orquesta BRIZA – Vengo Cantando</title>
<link rel="stylesheet" href="https://fonts.googleapis.com/css2?family=Exo+2:wght@400;500;800&display=swap">
<style>
  :root {
    --page: #ececea;
    --sunset-magenta: #b8306e;
    --sunset-rose: #d9584a;
    --sunset-orange: #ee8a2c;
    --sunset-gold: #f7b733;
    --sunset-yellow: #fcd34a;
    --wave-red: #c8262f;
    --wave-amber: #f2a51d;
    --title-white: #ffffff;
    --subtitle-ink: #2a1a12;
  }
  * { margin: 0; padding: 0; box-sizing: border-box; }
  html, body {
    width: 1200px;
    height: 800px;
    overflow: hidden;
    background: var(--page);
  }
  .canvas {
    position: relative;
    width: 1200px;
    height: 800px;
  }
  .disc {
    position: absolute;
    left: 0;
    top: 0;
    width: 1200px;
    height: 800px;
  }
  .band-name {
    font-family: "Exo 2", sans-serif;
    font-weight: 800;
    fill: var(--title-white);
  }
  .band-name__first { font-size: 46px; letter-spacing: 1px; }
  .band-name__second { font-size: 112px; letter-spacing: 4px; }
  .single-title {
    font-family: "Exo 2", sans-serif;
    font-weight: 500;
    font-size: 30px;
    fill: var(--subtitle-ink);
  }
</style>
</head>
<body>
<main class="canvas">
  <svg class="disc" viewBox="0 0 1200 800" xmlns="http://www.w3.org/2000/svg">
    <defs>
      <clipPath id="disc-face">
        <circle cx="600" cy="400" r="350"/>
      </clipPath>
      <linearGradient id="sunset-sky" x1="0" y1="0" x2="1" y2="1">
        <stop offset="0" stop-color="var(--sunset-magenta)"/>
        <stop offset="0.3" stop-color="var(--sunset-rose)"/>
        <stop offset="0.55" stop-color="var(--sunset-orange)"/>
        <stop offset="0.8" stop-color="var(--sunset-gold)"/>
        <stop offset="1" stop-color="var(--sunset-yellow)"/>
      </linearGradient>
      <linearGradient id="skyline-shade" x1="0" y1="0" x2="0" y2="1">
        <stop offset="0" stop-color="#5a2a1e" stop-opacity="0"/>
        <stop offset="0.5" stop-color="#6a2f1c" stop-opacity="0.45"/>
        <stop offset="1" stop-color="#f39a2a" stop-opacity="0.3"/>
      </linearGradient>
    </defs>

    <g clip-path="url(#disc-face)">
      <rect class="disc__photo" x="250" y="50" width="700" height="700" fill="url(#sunset-sky)"
            role="img" aria-label="Photo of a city skyline at sunset with lit towers along the lakeshore"/>
      <rect x="620" y="120" width="330" height="480" fill="url(#skyline-shade)"/>

      <path class="disc__wave disc__wave--red" d="M250 660 C420 600 640 560 950 470 L950 750 L250 750 Z" fill="var(--wave-red)" opacity="0.85"/>
      <path class="disc__wave disc__wave--amber" d="M250 700 C460 640 700 590 950 520 L950 750 L250 750 Z" fill="var(--wave-amber)"/>
      <path class="disc__wave disc__wave--yellow" d="M250 740 C480 690 720 640 950 590 L950 750 L250 750 Z" fill="var(--sunset-yellow)" opacity="0.9"/>
    </g>

    <circle class="disc__ring" cx="600" cy="400" r="336" fill="none" stroke="#ffffff" stroke-width="2"/>
    <circle class="disc__hole" cx="600" cy="400" r="50" fill="var(--page)"/>

    <text class="band-name band-name__first" x="330" y="245">Orquesta</text>
    <text class="band-name band-name__second" x="300" y="350">BRIZA</text>
    <text class="single-title" x="320" y="505">Vengo Cantando</text>
  </svg>
</main>
</body>
</html>
```